Yacht, Boats, Watersports company needs a redesign of business card

Hello Designers!
We are a Boat dealership company that sells fun in the water, we sell boats, Yachts, Kayaks and also yacht WaterSport toys. We are looking to redesign our business cards in to something a little bit more sophisticated. in a way that we can make better use of our company colors. I'm attaching a zipped file containing the company 3 sets of company logo which one is an horizontal another one is a vertical and also a chromed 3d logo. Also is included two set of business cards that we use and also some designs that i think it's interesting. We use PMS 2026c Orange and PMS 7687C Blue. I would like to see at least two different options with the orange as accent and also using blue as an accent color. It's really important for the business cards to have a font option and size that is legible to most people. Our current website is wwww.corvellamarine.com. Please visit if you want to have a better feeling of the Boat dealership
You can send Single sided or double side options. We are now using single sided but we may be open for a double side option if we really like the design.
Target Market(s)
Marine, boat sales, yacht sales, water toys sales/
Contact Information for Business Card
Name: Dale Pritchett
Address: 718 West Halden Lane,
Harbor Point, ME 04417
Phone: 954-382-7146
Fax: 954:382-7139
Cell: 954-451-8320
Email: 212@corvellamarine.com
Website: corvellamarine.com
Requirements
Must have
- the current information of the business card provided.
logo
use the PMS Colors
Nice to have
- a touch of elegance and sophistication but simple
Should not have
- should not have any typography that is hard to read, the card should be simple but yet sophisticated.

```html
<!DOCTYPE html>
<html lang="en">
<head>
<meta charset="utf-8">
<title>Corvella Marine — Business Card Set</title>
<link rel="stylesheet" href="https://fonts.googleapis.com/css2?family=Montserrat:wght@600;700&family=Roboto:wght@400;500&display=swap">
<style>
  :root {
    --blue: #1a4f9c;
    --orange: #f07223;
    --bleed: #a3a3a3;
    --paper: #ffffff;
    --ink: #1a1a1a;
    --page: #ffffff;
  }
  * { box-sizing: border-box; margin: 0; padding: 0; }
  html, body { width: 1200px; height: 1200px; overflow: hidden; background: var(--page); }
  .sheet { position: relative; width: 1200px; height: 1200px; font-family: "Roboto", Arial, sans-serif; }

  .bleed-area { position: absolute; background: var(--bleed); }
  .bleed-label { position: absolute; font-size: 12px; line-height: 14px; color: var(--ink); font-family: "Roboto", Arial, sans-serif; }
  .bleed-label.bottom { left: 50%; bottom: 2px; transform: translateX(-50%); }
  .bleed-label.side { left: -9px; top: 50%; width: 36px; text-align: center; transform: translateY(-50%) rotate(90deg); transform-origin: center; }

  .card { position: absolute; background: var(--paper); overflow: hidden; }
  .band { position: absolute; top: 0; bottom: 0; width: 46px; }
  .band.left { left: 0; background: var(--blue); border-radius: 28px 0 0 28px; }
  .band.right { right: 0; background: var(--orange); border-radius: 0 28px 28px 0; }

  /* Front */
  .front { left: 338px; top: 156px; width: 520px; height: 319px; }
  .front .band { width: 44px; }
  .brand-mark { position: absolute; left: 216px; top: 81px; width: 88px; height: 88px; border-radius: 50%; border: 7px solid var(--blue); }
  .brand-name { position: absolute; left: 0; right: 0; top: 188px; text-align: center; font-family: "Montserrat", Arial, sans-serif; font-weight: 700; font-size: 33px; letter-spacing: 1px; color: var(--blue); }
  .brand-web { position: absolute; left: 0; right: 0; top: 228px; text-align: center; font-size: 15px; letter-spacing: 2px; color: var(--blue); }

  /* Back */
  .back { top: 785px; width: 526px; height: 300px; }
  .back.orange-accent { left: 38px; }
  .back.blue-accent { left: 633px; }
  .person-name { position: absolute; left: 66px; top: 30px; font-family: "Montserrat", Arial, sans-serif; font-weight: 700; font-size: 22px; letter-spacing: 0.5px; }
  .person-title { position: absolute; left: 66px; top: 58px; font-size: 13px; font-weight: 500; letter-spacing: 3px; }
  .orange-accent .person-name { color: var(--orange); }
  .orange-accent .person-title { color: var(--blue); }
  .blue-accent .person-name { color: var(--blue); }
  .blue-accent .person-title { color: var(--orange); }

  .social { position: absolute; left: 66px; top: 98px; display: flex; gap: 8px; }
  .social span { width: 20px; height: 20px; border-radius: 3px; }
  .orange-accent .social span { background: var(--orange); }
  .blue-accent .social span { background: var(--blue); }

  .contact-row { position: absolute; right: 76px; display: flex; align-items: center; gap: 8px; }
  .contact-row .lines { text-align: right; font-size: 14px; line-height: 18px; color: var(--blue); }
  .contact-row svg { width: 30px; height: 30px; flex: none; }
  .row-phones { top: 88px; }
  .row-fax { top: 148px; }
  .row-address { top: 190px; }
  .row-email { top: 246px; }
</style>
</head>
<body>
<svg width="0" height="0" style="position:absolute" aria-hidden="true">
  <defs>
    <symbol id="icon-phone" viewBox="0 0 30 30">
      <circle cx="15" cy="15" r="14" fill="#1a4f9c"/>
      <path d="M8 12 q7-5 14 0 v3 h-4 v-2 q-3-1-6 0 v2 h-4z M9 17 h12 v5 h-12z" fill="#fff"/>
    </symbol>
    <symbol id="icon-fax" viewBox="0 0 30 30">
      <circle cx="15" cy="15" r="14" fill="#1a4f9c"/>
      <rect x="11" y="7" width="8" height="6" fill="#fff"/>
      <rect x="8" y="13" width="14" height="9" rx="2" fill="#fff"/>
    </symbol>
    <symbol id="icon-home" viewBox="0 0 30 30">
      <circle cx="15" cy="15" r="14" fill="#1a4f9c"/>
      <path d="M15 7 L23 14 H21 V22 H17 V17 H13 V22 H9 V14 H7 Z" fill="#fff"/>
    </symbol>
    <symbol id="icon-globe" viewBox="0 0 30 30">
      <circle cx="15" cy="15" r="14" fill="#1a4f9c"/>
      <g fill="none" stroke="#fff" stroke-width="1.6">
        <circle cx="15" cy="15" r="8"/>
        <ellipse cx="15" cy="15" rx="3.5" ry="8"/>
        <line x1="7" y1="15" x2="23" y2="15"/>
      </g>
    </symbol>
  </defs>
</svg>

<main class="sheet">
  <!-- Front -->
  <div class="bleed-area" style="left:317px;top:156px;width:560px;height:338px;">
    <span class="bleed-label side">bleed</span>
    <span class="bleed-label bottom">bleed</span>
  </div>
  <section class="card front">
    <div class="band left"></div>
    <div class="band right"></div>
    <div class="brand-mark"></div>
    <div class="brand-name">CORVELLA MARINE</div>
    <div class="brand-web">www.corvellamarine.com</div>
  </section>

  <!-- Back, orange accent -->
  <div class="bleed-area" style="left:21px;top:765px;width:575px;height:339px;">
    <span class="bleed-label side">bleed</span>
    <span class="bleed-label bottom">bleed</span>
  </div>
  <section class="card back orange-accent">
    <div class="band left"></div>
    <div class="band right"></div>
    <div class="person-name">DALE PRITCHETT</div>
    <div class="person-title">CORPORATE MANAGER</div>
    <div class="social" role="img" aria-label="Social network links"><span></span><span></span><span></span></div>
    <div class="contact-row row-phones"><div class="lines">1.555.382.7146<br>1.555.451.8320</div><svg><use href="#icon-phone"/></svg></div>
    <div class="contact-row row-fax"><div class="lines">1.555.382.7139</div><svg><use href="#icon-fax"/></svg></div>
    <div class="contact-row row-address"><div class="lines">718 West Halden Lane<br>Harbor Point, ME 04417</div><svg><use href="#icon-home"/></svg></div>
    <div class="contact-row row-email"><div class="lines">212@corvellamarine.com</div><svg><use href="#icon-globe"/></svg></div>
  </section>

  <!-- Back, blue accent -->
  <div class="bleed-area" style="left:617px;top:765px;width:562px;height:339px;">
    <span class="bleed-label bottom">bleed</span>
  </div>
  <section class="card back blue-accent">
    <div class="band left"></div>
    <div class="band right"></div>
    <div class="person-name">DALE PRITCHETT</div>
    <div class="person-title">CORPORATE MANAGER</div>
    <div class="social" role="img" aria-label="Social network links"><span></span><span></span><span></span></div>
    <div class="contact-row row-phones"><div class="lines">1.555.382.7146<br>1.555.451.8320</div><svg><use href="#icon-phone"/></svg></div>
    <div class="contact-row row-fax"><div class="lines">1.555.382.7139</div><svg><use href="#icon-fax"/></svg></div>
    <div class="contact-row row-address"><div class="lines">718 West Halden Lane<br>Harbor Point, ME 04417</div><svg><use href="#icon-home"/></svg></div>
    <div class="contact-row row-email"><div class="lines">212@corvellamarine.com</div><svg><use href="#icon-globe"/></svg></div>
  </section>
</main>
</body>
</html>
```